Banner Ad Needed for Auto Company
Animated banner needed.
Thanks everyone for your HARD work! It was a tough decision. Congrats to all of you on your amazing talents!
-GSC
I want submit design
We nee one ad, in the three sizes. They can all have the same style, look & feel.
You can just upload one design, when picking a winner comes to be the winner will just be required to send all 3 sizes.
I hope I was able to answer your question.
Thanks.
Hi just have a quick question. You need three ads and the three adds should be in each of the sizes you listed? So three ads and each ad is in three different sizes or three ads and the first ad is in the first size you gave, the second is in the second size and the third is in the third size?
I was just a little confused and just want some clarity.
Thanks!!!
Images & logo have been uploaded. Thanks!

```html
<!DOCTYPE html>
<html lang="en">
<head>
<meta charset="utf-8">
<title>Zippa Auto – Service Banner</title>
<link rel="stylesheet" href="https://fonts.googleapis.com/css2?family=PT+Serif:wght@400;700&display=swap">
<style>
  :root{
    --stage:#cdbd9c;
    --stage-edge:#e2d7c0;
    --brand-red:#d8121c;
    --white:#ffffff;
    --ink:#3a0a0c;
    --soft-pink:#f7c9cb;
    --cars-dark:#2b2d33;
    --cars-mid:#6d7079;
    --shop-blue:#3f5e86;
    --shop-dark:#1e2430;
  }
  *{box-sizing:border-box;margin:0;padding:0}
  html,body{width:1200px;height:367px;overflow:hidden}
  body{
    background:var(--stage);
    font-family:"PT Serif",Georgia,serif;
    color:var(--white);
    position:relative;
    box-shadow:inset 0 0 0 4px var(--stage-edge);
  }
  .frame{position:absolute;top:7px;width:384px;height:353px;display:grid}
  .frame--open{left:7px;grid-template-columns:221px 163px;grid-template-rows:166px 187px}
  .frame--offer{left:408px;grid-template-columns:221px 163px;grid-template-rows:173px 180px}
  .frame--visit{left:809px;grid-template-columns:163px 221px;grid-template-rows:173px 180px}

  .panel{background:var(--brand-red);position:relative}
  .photo{border-left:2px solid var(--white)}
  .photo--cars{background:linear-gradient(160deg,var(--cars-mid) 0%,var(--cars-dark) 55%,#8a1a1e 100%)}
  .photo--shop{background:linear-gradient(200deg,#7a8798 0%,var(--shop-blue) 45%,var(--shop-dark) 100%);border-top:2px solid var(--white)}
  .frame--visit .photo{border-left:none;border-right:2px solid var(--white)}

  /* frame 1 */
  .frame--open .panel{grid-row:1 / span 2}
  .frame--open .photo--cars{grid-column:2;grid-row:1}
  .frame--open .photo--shop{grid-column:2;grid-row:2}
  .brand{position:absolute;left:12px;top:22px;display:flex;align-items:center;gap:8px;
    font-weight:700;font-size:20px;line-height:1.05;width:190px}
  .brand__dot{width:14px;height:14px;border-radius:50%;background:var(--white);flex:none}
  .tagline{position:absolute;left:16px;top:150px;width:190px;display:flex;flex-direction:column;gap:4px}
  .tagline span{background:var(--white);color:var(--ink);font-size:18px;line-height:1.35;padding:0 5px;text-align:center}
  .headline-open{position:absolute;left:0;right:0;top:226px;text-align:center;font-weight:700;
    font-size:52px;line-height:1.08}

  /* frame 2 */
  .offer{position:absolute;left:26px;top:18px;font-weight:700}
  .offer__pct{font-size:66px;line-height:1}
  .offer__off{display:flex;align-items:center;gap:10px;font-size:40px;line-height:1}
  .offer__tick{width:34px;height:34px;background:var(--white)}
  .service{padding:22px 14px 0}
  .service__title{font-weight:700;font-size:21px;letter-spacing:.5px;margin-bottom:10px}
  .service__note{background:var(--white);color:var(--ink);font-size:17px;line-height:1.3;padding:4px 8px}

  /* frame 3 */
  .frame--visit .photo--cars{grid-column:1;grid-row:1}
  .frame--visit .photo--shop{grid-column:1;grid-row:2}
  .frame--visit .panel{grid-column:2;grid-row:1 / span 2;padding:24px 20px}
  .visit__headline{font-weight:700;font-size:33px;line-height:1.15;text-align:center}
  .visit__label{margin-top:64px;font-size:17px;color:var(--soft-pink)}
  .visit__address{margin-top:20px;font-size:17px;line-height:1.45;color:var(--soft-pink)}
</style>
</head>
<body>

<section class="frame frame--open">
  <div class="panel">
    <div class="brand"><span class="brand__dot"></span><span>Zippa Auto Group LLC</span></div>
    <p class="tagline"><span>Zippa Auto's</span><span>service department is</span></p>
    <h1 class="headline-open">NOW<br>OPEN!</h1>
  </div>
  <div class="photo photo--cars" role="img" aria-label="Row of parked cars on a dealership lot"></div>
  <div class="photo photo--shop" role="img" aria-label="Mechanic working under the hood of a car"></div>
</section>

<section class="frame frame--offer">
  <div class="panel">
    <div class="offer">
      <div class="offer__pct">10%</div>
      <div class="offer__off">OFF
        <svg class="offer__tick" viewBox="0 0 34 34" aria-hidden="true">
          <rect width="34" height="34" fill="#fff"/>
          <path d="M7 17 L14 25 L28 7" fill="none" stroke="#d8121c" stroke-width="4"/>
        </svg>
      </div>
    </div>
  </div>
  <div class="photo photo--cars" role="img" aria-label="Row of parked cars on a dealership lot"></div>
  <div class="panel service">
    <div class="service__title">ANY SERVICE</div>
    <p class="service__note">appointment booked online this weekend only.</p>
  </div>
  <div class="photo photo--shop" role="img" aria-label="Mechanic working under the hood of a car"></div>
</section>

<section class="frame frame--visit">
  <div class="photo photo--cars" role="img" aria-label="Row of parked cars on a dealership lot"></div>
  <div class="panel">
    <h2 class="visit__headline">We're right around the corner!</h2>
    <p class="visit__label">Visit us at</p>
    <p class="visit__address">12th and Maple St<br>in Denver..</p>
  </div>
  <div class="photo photo--shop" role="img" aria-label="Mechanic working under the hood of a car"></div>
</section>

</body>
</html>
```